Stationary for Marigold Spa
Business Card, Envelope, & Letterhead
Project: Stationary for Marigold Spa
Stationary for Marigold Spa -
Creative Brief
Simple
use logo no person's name
27815 Orchard Blvd. Ste 342 San Antonio, TX 78259
hbt4726@quillpost.net
We don't have the website yet. Please do not use the email on the project. On the business card front side, we only need our logo, address, phone no. Back side will be the services that we will provide.
Acupressure, Tui Na, Deep Tissue Massage, Swedish Massage, Prenatal Massage, Reflexology, Traditional Herbal Foot Treatment

```html
<!DOCTYPE html>
<html lang="en">
<head>
<meta charset="utf-8">
<title>Marigold Spa – Business Card</title>
<link rel="stylesheet" href="https://fonts.googleapis.com/css2?family=Questrial&display=swap">
<style>
  :root {
    --canvas-bg: #e9e7e3;
    --card-white: #ffffff;
    --ink-grey: #6f6f6f;
    --ink-dark: #3c3c34;
    --spa-green: #b3c12a;
    --curve-grey: #c9c9c9;
    --curve-grey-light: #e4e4e4;
  }
  html, body {
    margin: 0;
    padding: 0;
    width: 1200px;
    height: 646px;
    overflow: hidden;
    background: var(--canvas-bg);
    font-family: "Questrial", sans-serif;
  }
  .business-card {
    position: absolute;
    left: 100px;
    top: 37px;
    width: 1000px;
    height: 572px;
    background: var(--card-white);
    box-shadow: 0 6px 22px rgba(0,0,0,0.12);
    overflow: hidden;
  }
  .card-curves {
    position: absolute;
    inset: 0;
    width: 100%;
    height: 100%;
  }
  .brand {
    position: absolute;
    left: 250px;
    top: 150px;
    color: var(--ink-grey);
  }
  .brand-name {
    font-size: 66px;
    line-height: 1;
    letter-spacing: -1px;
    margin: 0;
    font-weight: 400;
  }
  .brand-tagline {
    font-size: 26px;
    color: var(--spa-green);
    margin: 6px 0 0 4px;
  }
  .phone {
    position: absolute;
    left: 255px;
    top: 292px;
    display: flex;
    align-items: center;
    gap: 16px;
    font-size: 40px;
    color: var(--ink-grey);
  }
  .phone-icon {
    width: 40px;
    height: 40px;
  }
  .address {
    position: absolute;
    left: 660px;
    top: 505px;
    transform: rotate(-22deg);
    transform-origin: left top;
    font-size: 19px;
    line-height: 1.5;
    font-style: normal;
    white-space: nowrap;
    color: var(--ink-dark);
  }
  .address p { margin: 0; }
</style>
</head>
<body>
  <main class="business-card">
    <svg class="card-curves" viewBox="0 0 1000 572" aria-hidden="true">
      <path d="M250 572 C 520 470, 760 360, 1000 250 L 1000 300 C 760 400, 540 500, 360 572 Z" fill="var(--curve-grey-light)"/>
      <path d="M330 572 C 560 480, 790 380, 1000 300 L 1000 330 C 800 410, 580 500, 400 572 Z" fill="var(--curve-grey)"/>
      <path d="M430 572 C 640 500, 830 410, 1000 340 L 1000 572 Z" fill="var(--spa-green)"/>
    </svg>

    <header class="brand">
      <h1 class="brand-name">Marigold Spa</h1>
      <p class="brand-tagline">Health Relaxation</p>
    </header>

    <div class="phone">
      <svg class="phone-icon" viewBox="0 0 40 40" aria-hidden="true">
        <circle cx="20" cy="20" r="17" fill="none" stroke="var(--spa-green)" stroke-width="3"/>
        <path d="M14 11 l4 0 l2 6 l-3 2 c1.5 3 3 4.5 6 6 l2-3 l6 2 l0 4 c-10 1 -18 -7 -17 -17 z" fill="var(--spa-green)"/>
      </svg>
      <span class="phone-number">(210) 555-0184</span>
    </div>

    <address class="address">
      <p>27815 Orchard Blvd.</p>
      <p>Ste 342 San Antonio, TX 78259</p>
    </address>
  </main>
</body>
</html>
```